Threshold
Business cards/letter head
Threshold - Consulting
Creative Brief
Use standard fonts
Maren Holt
3187 Wexbury Lane, Millbrook, OR 97034
Holt.maren@quillpost.example
please use a complementary font to the logo. logo art uploaded.

```html
<!DOCTYPE html>
<html lang="en">
<head>
<meta charset="utf-8">
<title>Threshold Stationery</title>
<link rel="stylesheet" href="https://fonts.googleapis.com/css2?family=Open+Sans:wght@300;400;600;700&display=swap">
<style>
:root{
  --backdrop:#5b5b5b;
  --paper:#ffffff;
  --charcoal:#3b3b3d;
  --ink:#333333;
  --accent:#e3d13f;
  --map-dark:#4f4e46;
  --map-yellow:#ecdf6a;
  --ring-faint:rgba(227,209,63,.14);
}
*{box-sizing:border-box;margin:0;padding:0}
html,body{width:1200px;height:1075px;overflow:hidden;background:var(--backdrop)}
body{position:relative;font-family:"Open Sans",Arial,sans-serif;color:var(--ink)}
.piece{position:absolute;overflow:hidden;box-shadow:0 2px 6px rgba(0,0,0,.35)}

/* logo lockup */
.lockup{position:absolute;display:flex;align-items:center;gap:8px;font-weight:300;letter-spacing:.5px;line-height:1;white-space:nowrap}
.lockup .dot{border-radius:50%;background:currentColor;flex:none}
.lockup--dark{color:var(--charcoal)}
.lockup--light{color:var(--paper)}

/* corner mark */
.corner-disc{position:absolute;border-radius:50%;background:var(--charcoal)}
.corner-ring{position:absolute;border-radius:50%;border:14px solid var(--accent)}

/* contact block */
.contact{position:absolute;font-size:11px;line-height:16px;color:var(--ink);white-space:nowrap}
.contact .name{font-size:19px;font-weight:600;margin-bottom:10px;color:var(--charcoal);line-height:24px}
.contact .gap{height:10px}
.contact .line{display:flex;align-items:center;gap:6px}
.icon{width:10px;height:10px;flex:none}

/* business card front */
.card-front{left:73px;top:35px;width:478px;height:287px;background:var(--paper)}
.card-front .lockup{right:28px;top:30px;font-size:30px}
.card-front .lockup .dot{width:22px;height:22px}
.card-front .corner-ring{left:-90px;bottom:-90px;width:200px;height:200px}
.card-front .corner-disc{left:-60px;bottom:-60px;width:140px;height:140px}
.card-front .contact{left:128px;top:80px}

/* business card back */
.card-back{left:568px;top:35px;width:510px;height:287px;background:var(--charcoal)}
.map-dark{position:absolute;left:20px;top:20px;width:400px;height:230px;background:radial-gradient(ellipse at 50% 50%,var(--map-dark) 0%,var(--charcoal) 75%)}
.card-back .lockup{right:26px;bottom:58px;font-size:32px}
.card-back .lockup .dot{width:24px;height:24px;background:var(--accent)}

/* letterhead */
.letterhead{left:73px;top:352px;width:484px;height:703px;background:var(--paper)}
.letterhead .lockup{right:26px;top:32px;font-size:28px}
.letterhead .lockup .dot{width:20px;height:20px}
.faint-ring{position:absolute;left:120px;top:250px;width:300px;height:300px;border-radius:50%;border:22px solid var(--ring-faint)}
.letter-body{position:absolute;left:40px;top:110px;width:400px;font-size:8.6px;line-height:12px;color:#444}
.letter-body p{margin-bottom:9px}
.recipient{margin-bottom:14px}
.signature{width:110px;height:26px;margin-top:4px;background:linear-gradient(90deg,rgba(80,80,80,.25),rgba(80,80,80,.05))}
.letterhead .corner-ring{left:-80px;bottom:-80px;width:180px;height:180px;border-width:12px}
.letterhead .corner-disc{left:-54px;bottom:-54px;width:126px;height:126px}
.letterhead .contact{left:120px;top:600px;font-size:9px;line-height:13px}
.letterhead .contact .gap{height:6px}

/* envelope back */
.envelope-back{left:574px;top:366px;width:504px;height:244px;background:var(--paper)}
.flap{position:absolute;left:0;top:0}
.envelope-back .mark{position:absolute;left:240px;top:70px;width:26px;height:26px;border-radius:50%;background:var(--paper)}

/* envelope front */
.envelope-front{left:574px;top:638px;width:504px;height:197px;background:var(--paper)}
.envelope-front .lockup{right:24px;top:24px;font-size:22px}
.envelope-front .lockup .dot{width:16px;height:16px}
.envelope-front .corner-ring{left:-70px;bottom:-70px;width:150px;height:150px;border-width:10px}
.envelope-front .corner-disc{left:-48px;bottom:-48px;width:106px;height:106px}
.envelope-front .contact{left:92px;top:128px;font-size:7.5px;line-height:11px}

/* yellow card */
.card-yellow{left:574px;top:867px;width:422px;height:188px;background:var(--accent)}
.map-yellow{position:absolute;left:20px;top:15px;width:300px;height:160px;background:radial-gradient(ellipse at 50% 50%,var(--map-yellow) 0%,var(--accent) 75%)}
.card-yellow .lockup{right:22px;bottom:34px;font-size:26px}
.card-yellow .lockup .dot{width:18px;height:18px}
</style>
</head>
<body>

<section class="piece card-front" aria-label="Business card front">
  <div class="lockup lockup--dark"><span class="dot"></span><span>threshold</span></div>
  <div class="corner-ring"></div>
  <div class="corner-disc"></div>
  <div class="contact">
    <div class="name">Maren Holt</div>
    <div>3187 Wexbury Lane</div>
    <div>Millbrook, OR 97034</div>
    <div class="gap"></div>
    <div class="line"><svg class="icon" viewBox="0 0 10 10"><rect width="10" height="10" rx="2" fill="#e3d13f"/><path d="M3 2.5h1.4l.6 1.6-.8.6a4 4 0 0 0 1.6 1.6l.6-.8 1.6.6V7.5A1 1 0 0 1 6.5 8.5 5 5 0 0 1 2 4 1 1 0 0 1 3 2.5z" fill="#fff"/></svg>+1 503 555 0148</div>
    <div class="line"><svg class="icon" viewBox="0 0 10 10"><rect width="10" height="10" rx="2" fill="#e3d13f"/><path d="M2 3h6v4H2z" fill="none" stroke="#fff" stroke-width=".9"/><path d="M2 3l3 2.2L8 3" fill="none" stroke="#fff" stroke-width=".9"/></svg>Holt.maren@quillpost.example</div>
  </div>
</section>

<section class="piece card-back" aria-label="Business card back">
  <div class="map-dark" role="img" aria-label="Dotted world map in muted olive tones"></div>
  <div class="lockup lockup--light"><span class="dot"></span><span>threshold</span></div>
</section>

<section class="piece letterhead" aria-label="Letterhead">
  <div class="lockup lockup--dark"><span class="dot"></span><span>threshold</span></div>
  <div class="faint-ring"></div>
  <div class="letter-body">
    <div class="recipient">
      <div>Mr. Tobias Lane</div>
      <div>Customer Service Manager</div>
      <div>Brightline Co.</div>
      <div>48 Harbor Way</div>
      <div>Fairview, OR 97024</div>
    </div>
    <p>Dear Mr. Lane,</p>
    <p>I was excited to see your opening for a customer service rep, and I hope to be invited for an interview.</p>
    <p>My background includes serving as a customer service associate within both high-volume and retail environments. Most recently, I worked on the customer service desk for Harbor Supply, where my responsibilities included resolving customer issues, processing returns, tracking orders, and handling inventory changes for flagged items to vendors and providing feedback to the team.</p>
    <p>Previously, I worked within a busy support center for a large telecommunications provider, where I answered calls, logged service tickets, and guided customers through setup steps, keeping an average of fifty calls per shift.</p>
    <p>In addition to this experience, I gained dependable customer service skills during my part-time work as a cashier and restaurant host while in high school.</p>
    <p>Sincerely,</p>
    <div class="signature" role="img" aria-label="Handwritten signature"></div>
  </div>
  <div class="corner-ring"></div>
  <div class="corner-disc"></div>
  <div class="contact">
    <div>3187 Wexbury Lane</div>
    <div>Millbrook, OR 97034</div>
    <div class="gap"></div>
    <div class="line"><svg class="icon" viewBox="0 0 10 10"><rect width="10" height="10" rx="2" fill="#e3d13f"/><path d="M3 2.5h1.4l.6 1.6-.8.6a4 4 0 0 0 1.6 1.6l.6-.8 1.6.6V7.5A1 1 0 0 1 6.5 8.5 5 5 0 0 1 2 4 1 1 0 0 1 3 2.5z" fill="#fff"/></svg>+1 503 555 0148</div>
    <div class="line"><svg class="icon" viewBox="0 0 10 10"><rect width="10" height="10" rx="2" fill="#e3d13f"/><path d="M2 3h6v4H2z" fill="none" stroke="#fff" stroke-width=".9"/><path d="M2 3l3 2.2L8 3" fill="none" stroke="#fff" stroke-width=".9"/></svg>Holt.maren@quillpost.example</div>
  </div>
</section>

<section class="piece envelope-back" aria-label="Envelope back">
  <svg class="flap" width="504" height="244" viewBox="0 0 504 244">
    <polygon points="0,0 504,0 504,18 252,140 0,18" fill="#3b3b3d"/>
    <polyline points="0,244 252,120 504,244" fill="none" stroke="#e2e2e2" stroke-width="1"/>
  </svg>
  <div class="mark"></div>
</section>

<section class="piece envelope-front" aria-label="Envelope front">
  <div class="lockup lockup--dark"><span class="dot"></span><span>threshold</span></div>
  <div class="corner-ring"></div>
  <div class="corner-disc"></div>
  <div class="contact">
    <div>3187 Wexbury Lane</div>
    <div>Millbrook, OR 97034</div>
  </div>
</section>

<section class="piece card-yellow" aria-label="Yellow card">
  <div class="map-yellow" role="img" aria-label="Faint world map in pale yellow"></div>
  <div class="lockup lockup--dark"><span class="dot"></span><span>threshold</span></div>
</section>

</body>
</html>
```